Bluestone Freight

We are a 3PL freight brokerage company looking to create a website to attract new customers. Some ideas on how other freight websites look is located at these links, https://www.marigoldhaulerline.com/services, https://quillmarkcargo.com/freight-brokerage/.
We would like to have a quote feature implemented into this website.

We specialize in heavy-haul, specialized loads, flatbed, and dry vans.

```html
<!DOCTYPE html>
<html lang="en">
<head>
<meta charset="utf-8">
<title>Bluestone Freight — Your Transportation Solution</title>
<link href="https://fonts.googleapis.com/css2?family=Montserrat:wght@400;500;600;700;800&display=swap" rel="stylesheet">
<style>
:root{
  --navy:#17276e;
  --navy-deep:#0f1c57;
  --gold:#b8962e;
  --gold-soft:#c9a640;
  --ink:#161616;
  --text:#3a3a3a;
  --white:#ffffff;
  --footer-bg:#f1f1f1;
}
*{margin:0;padding:0;box-sizing:border-box}
html,body{width:1200px;height:3529px;overflow:hidden}
body{font-family:'Montserrat',sans-serif;color:var(--ink);background:var(--white);position:relative}
.abs{position:absolute}
.brand{display:flex;align-items:center;gap:10px;font-weight:800;color:var(--navy);letter-spacing:.5px}
.brand-square{width:22px;height:22px;background:var(--gold)}
.social{display:flex;gap:10px}
.social span{width:36px;height:36px;border-radius:50%;background:var(--navy);display:block}
.social span:nth-child(2){background:var(--gold)}

/* header */
.site-header{top:0;left:0;width:1200px;height:130px;background:var(--white)}
.site-header .brand{position:absolute;left:10px;top:42px;font-size:26px}
.call{position:absolute;right:170px;top:32px;font-size:16px;font-weight:600;color:var(--gold)}
.call b{color:var(--ink)}
.site-header .social{position:absolute;right:12px;top:22px}
.nav{position:absolute;left:520px;top:84px;display:flex;gap:42px;font-size:15px;font-weight:500}
.nav a{color:var(--ink);text-decoration:none}
.nav a.active{color:var(--gold);border-bottom:2px solid var(--gold);padding-bottom:12px}
.btn-quote-top{position:absolute;right:12px;top:72px;background:var(--ink);color:var(--white);font-size:15px;font-weight:500;padding:10px 18px;border:2px solid var(--ink);outline:1px solid var(--white);outline-offset:-4px}

/* hero */
.hero{top:130px;left:0;width:1200px;height:600px;overflow:hidden}
.hero-photo{position:absolute;inset:0;background:linear-gradient(180deg,#d9a74a 0%,#9b7a3a 28%,#5f6a30 50%,#4c5a28 70%,#5b5d52 100%)}
.hero-shade{position:absolute;inset:0;background:linear-gradient(90deg,rgba(0,0,0,.35),rgba(0,0,0,0) 60%)}
.hero h1{position:absolute;left:134px;top:185px;color:var(--white);font-size:42px;font-weight:800;line-height:1.24;text-transform:uppercase}
.btn-gold{background:var(--gold);color:var(--white);font-size:14px;font-weight:500;padding:9px 18px;display:inline-block;outline:1px solid var(--white);outline-offset:-4px}
.hero .btn-gold{position:absolute;left:134px;top:375px}
.dots{position:absolute;right:130px;top:240px;display:flex;flex-direction:column;gap:8px}
.dots i{width:12px;height:12px;border:1.5px solid var(--white);border-radius:50%;display:block}
.dots i.on{background:radial-gradient(var(--white) 35%,transparent 40%)}
.hero svg{position:absolute;left:0;bottom:0}

/* section titles */
.ghost{position:absolute;font-size:60px;font-weight:500;color:transparent;-webkit-text-stroke:1px #e2e2e2;white-space:nowrap}
.eyebrow{position:absolute;font-size:15px;font-weight:600;color:var(--gold);display:flex;align-items:center;gap:10px}
.eyebrow::before{content:"";width:80px;height:1px;background:#cfcfcf}
.title{position:absolute;font-size:32px;font-weight:700;line-height:1.25}
.body-copy{position:absolute;font-size:13px;line-height:1.55;color:var(--text)}
.body-copy p{margin-bottom:16px}
.framed{position:absolute;border:1.5px solid #d9c08a;padding:14px;background:var(--white)}
.framed div{width:100%;height:100%}
.btn-dark{position:absolute;background:var(--ink);color:var(--white);font-size:13px;padding:10px 24px;outline:1px solid var(--white);outline-offset:-4px}

/* about */
.about{top:730px;left:0;width:1200px;height:600px}

/* services */
.services{top:1330px;left:0;width:1200px;height:940px}
.services .eyebrow::before{background:rgba(255,255,255,.3)}
.card{position:absolute;top:349px;width:283px;height:336px;overflow:hidden}
.card h3{position:absolute;left:28px;bottom:12px;color:var(--white);font-size:20px;font-weight:600}
.card.featured h3{top:165px;bottom:auto}
.card.featured p{position:absolute;left:28px;top:205px;width:220px;color:var(--white);font-size:12.5px;line-height:1.45}
.card.featured .btn-gold{position:absolute;left:28px;top:270px;font-size:12px;padding:7px 18px}

/* why */
.why{top:2270px;left:0;width:1200px;height:610px}

/* quote */
.quote{top:2880px;left:0;width:1200px;height:400px;background:var(--navy)}
.quote .ghost{-webkit-text-stroke:1px rgba(255,255,255,.14)}
.quote .eyebrow::before{background:rgba(255,255,255,.3)}
.field{position:absolute;border:1px solid rgba(255,255,255,.55);color:var(--white);font-size:11px;padding:8px 12px;height:34px}
.submit{position:absolute;left:530px;top:240px;width:140px;height:34px;background:var(--white);color:var(--navy);font-size:13px;text-align:center;line-height:34px;outline:1px solid var(--navy);outline-offset:-4px}
.quote svg{position:absolute;left:0;bottom:0}

/* footer */
.site-footer{top:3280px;left:0;width:1200px;height:249px;background:var(--footer-bg)}
.site-footer .brand{position:absolute;left:134px;top:88px;font-size:24px}
.col{position:absolute;top:38px}
.col h4{font-size:15px;font-weight:600;margin-bottom:18px}
.col li{list-style:none;font-size:11.5px;color:var(--text);margin-bottom:9px;display:flex;gap:8px;align-items:flex-start}
.col li.active{color:var(--gold)}
.col svg{flex:none;margin-top:1px}
.copy{position:absolute;left:134px;top:222px;font-size:11px;color:var(--text)}
.copy span{color:var(--gold)}
</style>
</head>
<body>

<header class="site-header abs">
  <div class="brand"><span class="brand-square"></span>Bluestone Freight</div>
  <div class="call">Call Us: <b>555.014.2290</b></div>
  <div class="social"><span></span><span></span><span></span></div>
  <nav class="nav">
    <a class="active" href="#">Home</a><a href="#">About Us</a><a href="#">Services</a><a href="#">Contact Us</a>
  </nav>
  <div class="btn-quote-top">Get a Free Quote</div>
</header>

<section class="hero abs">
  <div class="hero-photo" role="img" aria-label="Photo of a white freight truck driving along a highway through green hills at sunset"></div>
  <div class="hero-shade"></div>
  <h1>Your<br>Transportation<br>Solution</h1>
  <span class="btn-gold">Contact Us Today!</span>
  <div class="dots"><i></i><i class="on"></i><i></i><i></i></div>
  <svg width="1200" height="120" viewBox="0 0 1200 120">
    <polygon points="0,104 476,104 600,0 724,104 1200,104 1200,120 0,120" fill="var(--gold)"/>
    <polygon points="0,112 480,112 600,12 720,112 1200,112 1200,120 0,120" fill="var(--white)"/>
  </svg>
</section>

<section class="about abs">
  <div class="framed" style="left:133px;top:70px;width:452px;height:510px">
    <div role="img" aria-label="Photo of a smiling truck driver giving a thumbs up from the cab" style="background:linear-gradient(135deg,#8a6f5c,#c39478 45%,#d8703a 75%,#6e6a66)"></div>
  </div>
  <div class="ghost" style="left:651px;top:100px">About Us</div>
  <div class="eyebrow" style="left:651px;top:130px">About Us</div>
  <h2 class="title" style="left:651px;top:168px;width:440px">We are a full service Freight company</h2>
  <div class="body-copy" style="left:651px;top:270px;width:420px">
    <p>Lorem Ipsum is simply dummy text of the printing and typesetting industry.</p>
    <p>Lorem Ipsum has been the industry's standard dummy text ever since the 1500s, when an unknown printer took a galley of type and scrambled it to make a type specimen book.</p>
    <p>It has survived not only five centuries, but also the leap into electronic typesetting, remaining essentially unchanged. It was popularised in the 1960s with...</p>
  </div>
  <div class="btn-dark" style="left:651px;top:488px">Explore More</div>
</section>

<section class="services abs">
  <svg class="abs" style="left:0;top:0" width="1200" height="940" viewBox="0 0 1200 940">
    <polygon points="614,159 956,8 1200,115 1200,788 827,788 827,159" fill="var(--gold)"/>
    <polyline points="614,150 956,0 1200,106" fill="none" stroke="var(--navy-deep)" stroke-width="7"/>
    <polyline points="0,826 357,941 827,800" fill="none" stroke="var(--gold)" stroke-width="8"/>
    <polygon points="0,159 827,159 827,788 357,929 0,814" fill="var(--navy)"/>
  </svg>
  <div class="ghost" style="left:10px;top:220px;-webkit-text-stroke:1px rgba(255,255,255,.15)">Services</div>
  <div class="eyebrow" style="left:180px;top:230px">Our Services</div>
  <h2 class="title" style="left:89px;top:265px;color:var(--white)">What we do</h2>

  <div class="card" style="left:11px" role="img" aria-label="Photo of a purple heavy haul truck at dusk">
    <div style="position:absolute;inset:0;background:linear-gradient(160deg,#5a5fa0,#b86a70 55%,#3b2a48)"></div>
    <h3>Heavy Haul</h3>
  </div>
  <div class="card featured" style="left:310px" role="img" aria-label="Photo of an oversized industrial load on a trailer">
    <div style="position:absolute;inset:0;background:linear-gradient(160deg,#4a4a4a,#2c2c2c)"></div>
    <h3>Specialized Loads</h3>
    <p>Lorem Ipsum is simply dummy text of the printing and typesetting industry.</p>
    <span class="btn-gold">Read More</span>
  </div>
  <div class="card" style="left:609px" role="img" aria-label="Photo of a blue flatbed truck carrying timber">
    <div style="position:absolute;inset:0;background:linear-gradient(160deg,#9bb0c8,#2f4f96 55%,#4a3f38)"></div>
    <h3>Flatbed</h3>
  </div>
  <div class="card" style="left:907px" role="img" aria-label="Photo of a white dry van truck on a snowy road">
    <div style="position:absolute;inset:0;background:linear-gradient(160deg,#c9cdd8,#8a8fa4 55%,#6b6678)"></div>
    <h3>Dry Vans</h3>
  </div>
</section>

<section class="why abs">
  <div class="ghost" style="left:134px;top:100px">Why Bluestone Freight</div>
  <div class="eyebrow" style="left:134px;top:130px">Why Bluestone Freight?</div>
  <h2 class="title" style="left:134px;top:168px;width:420px">Experience &amp; Commitment!</h2>
  <div class="body-copy" style="left:134px;top:270px;width:420px">
    <p>Lorem Ipsum is simply dummy text of the printing and typesetting industry.</p>
    <p>Lorem Ipsum has been the industry's standard dummy text ever since the 1500s, when an unknown printer took a galley of type and scrambled it to make a type specimen book.</p>
    <p>It has survived not only five centuries, but also the leap into electronic typesetting, remaining essentially unchanged. It was popularised in the 1960s with...</p>
  </div>
  <span class="btn-gold abs" style="left:134px;top:485px">Explore More</span>
  <div class="framed" style="left:616px;top:50px;width:450px;height:510px">
    <div role="img" aria-label="Photo of a business handshake over trucks on a road with logistics network graphics" style="background:linear-gradient(160deg,#5a7fb8,#3a5a9c 45%,#d99a4a 75%,#2a3450)"></div>
  </div>
</section>

<section class="quote abs">
  <div class="ghost" style="left:415px;top:20px">Free Quote</div>
  <div class="eyebrow" style="left:495px;top:45px">Get a Free Quote</div>
  <div class="field" style="left:244px;top:90px;width:225px">Your Name</div>
  <div class="field" style="left:487px;top:90px;width:225px">Email</div>
  <div class="field" style="left:729px;top:90px;width:228px">Phone</div>
  <div class="field" style="left:244px;top:138px;width:713px;height:86px">Message ...</div>
  <div class="submit">Submit</div>
  <svg width="1200" height="110" viewBox="0 0 1200 110">
    <polygon points="0,102 472,102 600,0 728,102 1200,102 1200,110 0,110" fill="var(--gold)"/>
    <polygon points="478,110 600,12 722,110" fill="var(--white)"/>
  </svg>
</section>

<footer class="site-footer abs">
  <div class="brand"><span class="brand-square"></span>Bluestone Freight</div>
  <div class="col" style="left:415px">
    <h4>Contact Us</h4>
    <ul>
      <li><svg width="10" height="12" viewBox="0 0 10 12"><path d="M5 0a4 4 0 0 0-4 4c0 3 4 8 4 8s4-5 4-8a4 4 0 0 0-4-4zm0 5.5a1.5 1.5 0 1 1 0-3 1.5 1.5 0 0 1 0 3z" fill="var(--gold)"/></svg>Harbor Line Road, Millbrook,<br>ON A1B 2C3</li>
      <li><svg width="11" height="11" viewBox="0 0 11 11"><path d="M2 0l2 2.5-1 1.5c.8 1.6 2 2.8 3.5 3.5l1.5-1L10.5 8 9 10.5C4 10 .5 6.5 0 2z" fill="var(--gold)"/></svg>555.014.2290</li>
      <li><svg width="12" height="10" viewBox="0 0 12 10"><rect x=".5" y=".5" width="11" height="9" fill="none" stroke="var(--gold)"/><path d="M.5.5 6 5.5 11.5.5" fill="none" stroke="var(--gold)"/></svg>info@bluestonefreight.com</li>
    </ul>
  </div>
  <div class="col" style="left:707px">
    <h4>Quick Links</h4>
    <ul><li class="active">Home</li><li>About Us</li><li>Services</li><li>Contact Us</li></ul>
  </div>
  <div class="col" style="left:894px">
    <h4>Follow Us</h4>
    <div class="social"><span></span><span></span><span></span></div>
  </div>
  <svg class="abs" style="left:1117px;top:170px" width="20" height="20" viewBox="0 0 20 20"><path d="M4 16 10 4l6 12M7 11h6" fill="none" stroke="var(--navy)" stroke-width="1.6"/></svg>
  <div class="copy">© 2022 <span>Bluestone Freight</span>. All Right Reserved</div>
</footer>

</body>
</html>
```